Thai Restaurant Billboard Design

Design a billboard promoting food delivery during this Coronavirus time. We want to grab attention by embracing the Coronavirus and offering food delivery. People are sitting at home and this is the right time to promote food delivery.

I have the logo and spec sheet attached.

Target Market(s)

Anyone.

Requirements
Must have
• Top Heading should be big and bold:

Coronavirus Got You Quarantined?

Then put under

We Deliver
Healthy Thai Food!
Put the logo that is attached
415-283-6071
Nice to have
• Eyecatching. Creative.
Should not have
• Don't have any not haves. Make it look good.

```html
<!DOCTYPE html>
<html lang="en">
<head>
<meta charset="UTF-8">
<title>Siam Lotus House – Delivery Billboard</title>
<link rel="stylesheet" href="https://fonts.googleapis.com/css2?family=Almendra:wght@700&family=Marcellus+SC&display=swap">
<style>
  :root {
    --page-bg: #e6e8ea;
    --board-black: #000000;
    --headline-yellow: #ffd500;
    --text-white: #ffffff;
    --wood-dark: #221b17;
    --wood-mid: #3a2f29;
    --kraft: #a8825d;
    --kraft-light: #d9c2a4;
    --food-warm: #c9784f;
  }
  * { margin: 0; padding: 0; box-sizing: border-box; }
  html, body {
    width: 1200px;
    height: 801px;
    overflow: hidden;
    background: var(--page-bg);
  }
  .billboard {
    position: absolute;
    left: 0;
    top: 200px;
    width: 1200px;
    height: 400px;
    display: block;
  }
  .display-text {
    font-family: "Almendra", serif;
    font-weight: 700;
  }
  .headline { fill: var(--headline-yellow); font-size: 64px; }
  .subhead { fill: var(--text-white); font-size: 33px; }
  .tagline {
    fill: var(--headline-yellow);
    font-family: "Marcellus SC", serif;
    font-size: 26px;
  }
  .phone { fill: var(--text-white); font-size: 52px; }
  .brand-name { fill: var(--text-white); font-size: 15px; }
  .brand-mark { fill: none; stroke: var(--text-white); stroke-width: 2; }
</style>
</head>
<body>
  <svg class="billboard" viewBox="0 0 1200 400" xmlns="http://www.w3.org/2000/svg">
    <defs>
      <linearGradient id="wood-fade" x1="0" y1="0" x2="1" y2="0">
        <stop offset="0" stop-color="var(--board-black)"/>
        <stop offset="0.15" stop-color="var(--wood-dark)"/>
        <stop offset="0.6" stop-color="var(--wood-mid)"/>
        <stop offset="1" stop-color="var(--wood-dark)"/>
      </linearGradient>
      <radialGradient id="food-tones" cx="0.55" cy="0.45" r="0.65">
        <stop offset="0" stop-color="var(--food-warm)"/>
        <stop offset="0.35" stop-color="var(--kraft-light)"/>
        <stop offset="0.75" stop-color="var(--kraft)"/>
        <stop offset="1" stop-color="var(--wood-mid)"/>
      </radialGradient>
    </defs>

    <rect class="board-bg" width="1200" height="400" fill="var(--board-black)"/>

    <g class="food-photo" role="img" aria-label="Photo of two open kraft takeout boxes filled with Thai stir-fried noodles and seafood, with wooden chopsticks on a dark wood table">
      <rect x="580" y="0" width="620" height="400" fill="url(#wood-fade)"/>
      <rect x="650" y="28" width="505" height="355" rx="18" fill="url(#food-tones)"/>
    </g>

    <text class="display-text headline" x="52" y="100" textLength="551" lengthAdjust="spacingAndGlyphs">Coronavirus Got</text>
    <text class="display-text headline" x="52" y="172" textLength="588" lengthAdjust="spacingAndGlyphs">You Quarantined?</text>
    <text class="display-text subhead" x="48" y="222" textLength="592" lengthAdjust="spacingAndGlyphs">We Deliver Healthy Thai Food!</text>

    <rect class="brand-mark" x="72" y="250" width="72" height="72"/>
    <text class="display-text brand-name" x="108" y="350" text-anchor="middle" textLength="132" lengthAdjust="spacingAndGlyphs">Siam Lotus House</text>

    <text class="tagline" x="636" y="290" text-anchor="end" textLength="340" lengthAdjust="spacingAndGlyphs">Stay safe...eat well!</text>
    <text class="display-text phone" x="292" y="350" textLength="344" lengthAdjust="spacingAndGlyphs">415-283-6071</text>
  </svg>
</body>
</html>
```